Italian Restaurant Responsive Wordpress Website Design

Italian Restaurant is looking to create a new responsive website design based on some Wordpress templates that have been selected as favourites. We want to base the influence of the design off a business card that was recently created (attached below).
The design should be based of these templates that will be purchased when selected. All templates are responsive. Please read details of templates to learn more about their functions and features. After we select the designs we can deliver the customizable PSD files.
http://layoutgrove.example/item/tangle-responsive-restaurant-wordpress-theme/full_screen_preview/7316420
http://cloakdesigns.example/themes/?theme=Bellamo
http://themes.loftbrick.example/rigatta/
http://www.tablecraftkit.example/
Pages required
Homepage
-Navigation
-Contact info always accessible on all responsive viewports. You may have to include a design for Contact info on mobile viewport to the top of the page.
-Hours of Operation
About Page
Menu
-Styling of content will be very identical to menu's. That will be provided once I receive a copy.
Gallery
Contact Page
-Show a map, Contact Details and a Contact/Feedback Form
We are open to any designs that you want to lay on top of these Template designs. The current site is: www.quintavela.example If you want an indication of content.
Any questions please ask! Enjoy!
Updates
Hello Everyone. I just updated the menu being used in the restaurant as well as the fonts that are being used as we speak. Any questions please email me. Cheers.
Target Market(s)
The Target Market is families and a more distinguished crowd. They offer valued gourmet food but are located in a very high end neighbourhood. Want to deliver home made cuisine that's approachable but yet considered gourmet.
Industry/Entity Type
Business
Look and feel
Each slider illustrates characteristics of the customer's brand and the style your logo design should communicate.

```html
<!DOCTYPE html>
<html lang="en">
<head>
<meta charset="utf-8">
<title>Quinta Vela — Italian Restaurant</title>
<link href="https://fonts.googleapis.com/css2?family=Fjalla+One&family=Source+Sans+3:wght@300;400;600&family=PT+Sans+Narrow:wght@400;700&display=swap" rel="stylesheet">
<style>
:root{
  --red:#a3261a;
  --red-deep:#8e1e14;
  --red-text:#b32d1e;
  --pink-top:#f6d8d0;
  --pink-bot:#e8ada0;
  --nav-text:#9a2418;
  --grey-bg:#efefef;
  --text:#777;
  --dark:#333;
  --line:#ddd;
  --btn:#f4c9bd;
}
*{box-sizing:border-box;margin:0;padding:0}
html,body{width:970px;height:1200px;overflow:hidden;background:#fff}
body{position:relative;font-family:"Source Sans 3",sans-serif;color:var(--text)}
.site-header{position:absolute;left:0;top:0;width:970px;height:135px;background:linear-gradient(var(--pink-top),var(--pink-bot))}
.contact-info{position:absolute;right:52px;top:20px;text-align:right;font-size:12px;line-height:19px;color:#6b3a32;font-weight:300}
.contact-info .phone{font-size:16px;color:#4a1f19;font-weight:400}
.main-nav{position:absolute;top:86px;height:50px;display:flex;background:linear-gradient(#f5d5cc,#eab8ab);border:1px solid #f7e1db}
.main-nav a{display:block;padding:0 20px;line-height:48px;font-family:"PT Sans Narrow",sans-serif;font-size:17px;color:var(--nav-text);text-decoration:none;border-right:1px solid #dca396}
.main-nav a:last-child{border-right:0}
.nav-left{left:45px;width:300px}
.nav-right{left:615px;width:310px}
.brand{position:absolute;left:408px;top:24px;width:154px;height:154px;border-radius:50%;background:var(--red);border:6px solid #f6dcd5;display:flex;align-items:center;justify-content:center;z-index:3}
.brand span{font-family:"Source Sans 3",sans-serif;font-weight:600;font-size:23px;color:#fff}
.hero{position:absolute;left:0;top:135px;width:970px;height:384px;background:radial-gradient(ellipse at 55% 50%,#d9b37a 0%,#b86a35 40%,#7a3a1c 75%,#4a1e10 100%)}
.hero-caption{position:absolute;left:204px;top:203px;width:564px;height:94px;background:rgba(25,20,15,.75);text-align:center;color:#fff;font-family:"Fjalla One",sans-serif}
.hero-caption h1{font-weight:400;font-size:26px;margin-top:20px;letter-spacing:.3px}
.hero-caption p{font-size:17px;margin-top:2px}
.dots{position:absolute;left:460px;top:362px;display:flex;gap:3px}
.dots i{width:11px;height:11px;border-radius:50%;background:#fff}
.features{position:absolute;left:0;top:519px;width:970px;height:298px;background:var(--grey-bg)}
.card{position:absolute;top:31px;width:210px;height:233px;background:var(--red);border:1px solid #c94a3a;text-align:center;color:#fff}
.card .photo{height:103px}
.card h3{font-weight:400;font-size:17px;margin-top:9px}
.card p{font-size:11px;line-height:15px;font-weight:300;margin:4px 14px 0}
.card .btn{display:inline-block;margin-top:12px;background:var(--btn);color:var(--red-deep);font-family:"PT Sans Narrow",sans-serif;font-weight:700;font-size:11px;padding:4px 12px;border-radius:2px}
h2{font-weight:300;font-size:22px;color:var(--dark)}
.welcome{position:absolute;left:49px;top:848px;width:270px}
.welcome h2{color:var(--red-text)}
.welcome h2 b{font-weight:400}
.welcome p{font-size:12px;line-height:19px;margin-top:12px;font-weight:300}
.welcome p+p{margin-top:4px}
.news{position:absolute;left:370px;top:848px;width:270px}
.news-item{display:flex;gap:13px;margin-top:12px}
.news-item + .news-item{margin-top:20px}
.news-item .thumb{flex:0 0 76px;height:64px}
.news-item h4{font-weight:400;font-size:13px;color:var(--dark)}
.news-item p{font-size:11px;line-height:19px;font-weight:300;margin-top:2px}
.news-item .date{color:var(--red-text);font-weight:400;font-size:11px;margin-top:2px}
.hours{position:absolute;left:670px;top:848px;width:247px}
.hours table{width:100%;border-collapse:collapse;margin-top:10px;font-size:12px}
.hours td{height:26px;border-bottom:1px solid var(--line)}
.hours tr:last-child td{border-bottom:0}
.hours td.day{color:var(--red-text);padding-left:14px;position:relative}
.hours td.day::before{content:"";position:absolute;left:3px;top:9px;border-left:5px solid var(--red-text);border-top:4px solid transparent;border-bottom:4px solid transparent}
.hours td.time{color:var(--dark);width:118px}
.site-footer{position:absolute;left:0;top:1131px;width:970px;height:69px;border-top:1px solid #e4e4e4;background:#fff}
.site-footer p{position:absolute;left:53px;top:21px;font-size:12px;color:#666;font-weight:300}
.social{position:absolute;right:58px;top:18px;display:flex;gap:8px}
.social i{width:21px;height:21px;border-radius:2px}
</style>
</head>
<body>
<header class="site-header">
  <div class="contact-info">218 Larchmont Ave.<br>W. Harbourview, ON<br><span class="phone">(555) 014-2290</span></div>
  <nav class="main-nav nav-left"><a href="#">HOME</a><a href="#">MENUS</a><a href="#">GALLERY</a></nav>
  <nav class="main-nav nav-right" style="justify-content:flex-end"><a href="#">GROUPS</a><a href="#">VIP LIST</a><a href="#">CONTACT</a></nav>
  <div class="brand"><span>Quinta Vela</span></div>
</header>

<section class="hero" role="img" aria-label="Platter of nachos, quesadilla wedges and dips">
  <div class="hero-caption">
    <h1>DUIS TINCIDUNT LECTUS QUIS DUI VIVERRA</h1>
    <p>SUSPENDISSE VULPUTATE ALIQUAM DUI</p>
  </div>
  <div class="dots"><i></i><i></i><i></i><i></i></div>
</section>

<section class="features">
  <article class="card" style="left:50px">
    <div class="photo" role="img" aria-label="Grilled meat dish on a plate" style="background:linear-gradient(#c9b8a8,#6b4a32)"></div>
    <h3>What Special About Us</h3>
    <p>Marrowby's has relaunched this 35 year old American brand in a format that will excite both consumers</p>
    <span class="btn">LEARN MORE</span>
  </article>
  <article class="card" style="left:272px">
    <div class="photo" role="img" aria-label="Fresh noodle salad" style="background:linear-gradient(#e8e4dc,#d6a868)"></div>
    <h3>Health Breakfast</h3>
    <p>Marrowby's has relaunched this 35 year old American brand in a format that will excite both consumers</p>
    <span class="btn">LEARN MORE</span>
  </article>
  <article class="card" style="left:493px">
    <div class="photo" role="img" aria-label="Rice dish in a dark bowl" style="background:linear-gradient(#7a5a4a,#c9a89a)"></div>
    <h3>Order Now</h3>
    <p>Marrowby's has relaunched this 35 year old American brand in a format that will excite both consumers</p>
    <span class="btn">LEARN MORE</span>
  </article>
  <article class="card" style="left:715px">
    <div class="photo" role="img" aria-label="Glazed grilled fish with greens" style="background:linear-gradient(#e8ece4,#8a3a22 60%,#5a8a3a)"></div>
    <h3>Check Out Latest Dishes</h3>
    <p>Marrowby's has relaunched this 35 year old American brand in a format that will excite both consumers</p>
    <span class="btn">LEARN MORE</span>
  </article>
</section>

<section class="welcome">
  <h2>Welcome to <b>Quinta Vela</b></h2>
  <p>Located in the heart of Larchmont West, Quinta Vela is named for the most highly - refined italian flour, our key ingredient in our superior pizza and pasta. Santoro's pride &amp; joy: an Italian joint</p>
  <p>showcasing his Barese heritage. Our menu consists mostly of comfort food, offering a restaurant atmosphere for families and making it a tradition. We offer gluten free and whole-wheat options for our Wood Burning pizza and pasta. We cater to everyone, whether your want penne with butter</p>
</section>

<section class="news">
  <h2>Recent News</h2>
  <div class="news-item">
    <div class="thumb" role="img" aria-label="Plated seafood dish" style="background:linear-gradient(#d89a6a,#9a3a1e)"></div>
    <div><h4>Vivamus porttitor g purus</h4><p>Morbi eget arcu. Morbi porta, libero id ullamcorper nonummy nibh</p><p class="date">Posted on 25 October 2013</p></div>
  </div>
  <div class="news-item">
    <div class="thumb" role="img" aria-label="Salad with grilled meat" style="background:linear-gradient(#6a7a4a,#3a2a1e)"></div>
    <div><h4>Duis tincidunt lectus</h4><p>Donec scelerisque leo ac risus. Praesent sit amet est. In dictum, dolor eu dictum porttitor, enim</p><p class="date">Posted on 30 October 2013</p></div>
  </div>
</section>

<section class="hours">
  <h2>Operating Hours</h2>
  <table>
    <tr><td class="day">Monday :</td><td class="time">11:00am-10:00pm</td></tr>
    <tr><td class="day">Tuesday :</td><td class="time">11:00am-10:00pm</td></tr>
    <tr><td class="day">Wednesday :</td><td class="time">11:00am-11:00pm</td></tr>
    <tr><td class="day">Thursday :</td><td class="time">11:00am-11:00pm</td></tr>
    <tr><td class="day">Friday :</td><td class="time">11:00am-11:00pm</td></tr>
    <tr><td class="day">Saturday :</td><td class="time">11:00am-11:00pm</td></tr>
    <tr><td class="day">Sunday :</td><td class="time">4:30pm - 10pm</td></tr>
  </table>
</section>

<footer class="site-footer">
  <p>© 2013 Company Name.&nbsp; All right reserved.&nbsp; Term of Use</p>
  <div class="social" aria-label="Social links">
    <i style="background:#3b5a9a"></i><i style="background:#3fa9d8"></i><i style="background:#1a6aa0"></i><i style="background:#f08a24"></i>
  </div>
</footer>
</body>
</html>
```